Business Card Design

wig manufacturer
I would like something very upscale.highend looking
maybe mat chrome card with shiney chrome
or something like the Quorix business card very clean and simple white with the logo in silver
Target Market(s)
upscale women
Industry/Entity Type
Business
Contact Information for Business Card
OUR LOGO
company name:Marisol Tresses
48E52Street Dennis Holcroft
New York,N.Y 10018
Tel:646-5817730
1800-4369185
email:hairloft@zentrimail.com
website:Marisoltresses.com
Look and feel
Each slider illustrates characteristics of the customer's brand and the style your logo design should communicate.

```html
<!DOCTYPE html>
<html lang="en">
<head>
<meta charset="utf-8">
<title>Marisol Tresses – Business Card</title>
<link rel="stylesheet" href="https://fonts.googleapis.com/css2?family=Gelasio:wght@400&display=swap">
<style>
  :root {
    --stage: #d9d9d9;
    --card-black: #080808;
    --band-black: #141414;
    --band-black-light: #1c1c1c;
    --band-lower: #0d0d0d;
    --pattern-deep: #121212;
    --pattern-mid: #2a2a2a;
    --sheen: rgba(255, 255, 255, 0.07);
    --edge-light: #2e2e2e;
    --edge-dark: #050505;
    --text-silver: #e6e6e6;
    --accent-blue: #34509a;
  }
  html, body {
    margin: 0;
    width: 1200px;
    height: 900px;
    overflow: hidden;
    background: var(--stage);
  }
  .stage {
    width: 1200px;
    height: 900px;
    display: flex;
    align-items: center;
    justify-content: center;
  }
  .business-card {
    position: relative;
    width: 1000px;
    height: 572px;
    background: var(--card-black);
    overflow: hidden;
    font-family: "Gelasio", Georgia, serif;
    color: var(--text-silver);
    box-shadow: 0 18px 40px rgba(0, 0, 0, 0.35);
  }
  .damask-band {
    position: absolute;
    left: 0;
    width: 100%;
  }
  .damask-band--top {
    top: 0;
    height: 17%;
    background: radial-gradient(ellipse 70% 140% at 55% 30%, var(--pattern-mid), var(--pattern-deep));
  }
  .damask-band--bottom {
    bottom: 0;
    height: 30%;
    background: radial-gradient(ellipse 80% 120% at 35% 70%, var(--pattern-mid), var(--pattern-deep));
  }
  .info-band {
    position: absolute;
    left: 0;
    top: 17%;
    width: 100%;
    height: 41%;
    background: linear-gradient(180deg, var(--band-black-light) 0%, var(--band-black) 45%, #101010 100%);
    border-top: 2px solid var(--edge-light);
    border-bottom: 2px solid var(--edge-dark);
    box-shadow: 0 6px 14px rgba(0, 0, 0, 0.6), 0 -6px 14px rgba(0, 0, 0, 0.6);
  }
  .info-band__sheen {
    position: absolute;
    inset: 0;
    background: linear-gradient(100deg, transparent 30%, var(--sheen) 55%, transparent 80%);
  }
  .lower-band {
    position: absolute;
    left: 0;
    top: 58%;
    width: 100%;
    height: 12%;
    background: linear-gradient(180deg, #0a0a0a, var(--band-lower));
    border-bottom: 1px solid var(--edge-light);
    box-shadow: 0 4px 10px rgba(0, 0, 0, 0.55);
  }
  .brand-mark {
    position: absolute;
    left: 90px;
    top: 140px;
    height: 200px;
    display: flex;
    align-items: center;
    gap: 16px;
    font-size: 28px;
    color: var(--text-silver);
  }
  .brand-mark__dot {
    width: 58px;
    height: 58px;
    border-radius: 50%;
    background: var(--accent-blue);
  }
  .contact {
    position: absolute;
    left: 400px;
    top: 128px;
    width: 570px;
    text-align: center;
  }
  .contact__name {
    margin: 0 0 12px;
    font-size: 40px;
    font-weight: 400;
    letter-spacing: 1.5px;
  }
  .contact__line {
    margin: 0;
    font-size: 21px;
    line-height: 1.3;
  }
</style>
</head>
<body>
  <main class="stage">
    <article class="business-card">
      <div class="damask-band damask-band--top" role="img" aria-label="Dark damask floral pattern band"></div>
      <div class="info-band"><div class="info-band__sheen"></div></div>
      <div class="lower-band"></div>
      <div class="damask-band damask-band--bottom" role="img" aria-label="Dark damask floral pattern band"></div>

      <div class="brand-mark">
        <span class="brand-mark__dot"></span>
        <span class="brand-mark__name">Marisol Tresses</span>
      </div>

      <div class="contact">
        <h1 class="contact__name">MARISOL TRESSES</h1>
        <p class="contact__line">Tel: 646-5817730 1800-4369185</p>
        <p class="contact__line">email: hairloft@zentrimail.com web: Marisoltresses.com</p>
        <p class="contact__line">48E52Street Dennis Holcroft New York,N.Y 10018</p>
      </div>
    </article>
  </main>
</body>
</html>
```